Professional Learning Organization for Educators needs a Design Thinking Workshop Flyer

We need a flyer for a series of Introductory Design Thinking workshops we're delivering for education leaders.

We have generated our own version of the flyer with a word template, but want it to look even more professional and eye catching. It is attached.

We had an image that we thought might be good, but pulled it out so we don't bias designers' thinking.
Updates

Reason: We are a bit flexible on the deadline since this is a holiday week and people are traveling

Target Market(s)

Very busy education leaders whose curiosity needs to be stimulated enough to enroll in the course

Industry/Entity Type

Education

Font styles to use
Other font styles liked:
• Century Gothic or something closer to that

Requirements
Must have
• Some version of the text that is on the current flyer that I attached.
Nice to have
• I am very flexible and open right now on this design.

```html
<!DOCTYPE html>
<html lang="en">
<head>
<meta charset="utf-8">
<title>Design Thinking Course Flyer</title>
<link rel="stylesheet" href="https://fonts.googleapis.com/css2?family=Roboto:ital,wght@0,400;0,500;0,700;0,900;1,700;1,900&family=Roboto+Condensed:wght@400;700&family=Pacifico&display=swap">
<style>
  :root {
    --backdrop: #2e2520;
    --hero-blue: #0f3f66;
    --hero-blue-light: #1b6496;
    --band-red: #e54a33;
    --lime: #b8d334;
    --panel-blue: #0c5e88;
    --schedule-yellow: #f2e52a;
    --ink: #1c1c1c;
    --link-blue: #2d4fa0;
    --footer-blue: #1d6a93;
    --footer-cyan: #3fb2e4;
    --white: #ffffff;
    --black: #000000;
  }
  * { box-sizing: border-box; margin: 0; padding: 0; }
  html, body {
    width: 1200px; height: 1200px; overflow: hidden;
    background: var(--backdrop);
  }
  .flyer {
    position: absolute; left: 159px; top: 30px;
    width: 882px; height: 1140px;
    background: var(--white);
    font-family: "Roboto", sans-serif;
    overflow: hidden;
  }
  .hero {
    position: absolute; left: 0; top: 0; width: 882px; height: 481px;
    background: radial-gradient(ellipse at 70% 40%, var(--hero-blue-light), var(--hero-blue) 75%);
  }
  .hero-art {
    position: absolute; left: 410px; top: 0; width: 472px; height: 481px;
    background: radial-gradient(ellipse at 50% 55%, #2a6f9e 0%, #1a5383 45%, rgba(15,63,102,0) 80%);
  }
  .title-design {
    position: absolute; left: 34px; top: 116px;
    color: var(--lime); font-size: 46px; font-weight: 400;
    letter-spacing: 23px; line-height: 1;
  }
  .title-band {
    position: absolute; left: 0; top: 164px; width: 440px; height: 68px;
    background: linear-gradient(90deg, var(--band-red) 70%, rgba(229,74,51,0));
  }
  .title-thinking {
    position: absolute; left: 34px; top: 156px;
    color: var(--white); font-size: 78px; font-weight: 900;
    letter-spacing: -2px; line-height: 1;
  }
  .title-course {
    position: absolute; left: 34px; top: 245px;
    color: var(--lime); font-size: 44px; font-weight: 700;
    letter-spacing: 14px; line-height: 1;
  }
  .tagline {
    position: absolute; color: var(--white); font-size: 38px; line-height: 1; font-weight: 400;
  }
  .tagline-one { left: 38px; top: 362px; }
  .tagline-two { left: 105px; top: 414px; font-size: 36px; }
  .tagline-two strong { font-weight: 900; font-style: italic; }

  .hosts {
    position: absolute; left: 36px; top: 511px;
    font-size: 30px; font-weight: 900; font-style: italic; color: var(--ink);
    letter-spacing: -0.5px; line-height: 1; white-space: nowrap;
  }
  .intro {
    position: absolute; left: 36px; top: 545px; width: 740px;
    font-size: 16px; line-height: 19px; color: var(--ink);
  }
  .benefits {
    position: absolute; left: 50px; top: 614px; width: 440px;
    list-style: none; font-size: 15.5px; line-height: 19px; color: var(--ink);
  }
  .benefits li { position: relative; padding-left: 16px; margin-bottom: 8px; }
  .benefits li::before {
    content: ""; position: absolute; left: 0; top: 6px;
    width: 8px; height: 8px; border-radius: 50%; background: var(--ink);
  }

  .schedule {
    position: absolute; left: 0; top: 772px; width: 517px; height: 262px;
    background: var(--panel-blue);
  }
  .schedule-heading {
    position: absolute; left: 40px; top: 16px;
    font-family: "Roboto Condensed", sans-serif; font-weight: 400;
    font-size: 28px; line-height: 34px; white-space: nowrap;
    color: var(--schedule-yellow);
  }
  .sessions {
    position: absolute; left: 54px; top: 92px; list-style: none;
    font-size: 19px; color: var(--white);
  }
  .sessions li { position: relative; height: 35px; padding-left: 12px; }
  .sessions li::before {
    content: ""; position: absolute; left: -2px; top: 8px;
    width: 7px; height: 7px; border-radius: 50%; background: var(--lime);
  }
  .sessions .day { display: inline-block; width: 120px; }
  .sessions .start { display: inline-block; width: 112px; }
  .schedule-note {
    position: absolute; left: 36px; top: 234px; width: 475px;
    font-family: "Roboto Condensed", sans-serif; font-weight: 700;
    font-size: 13.5px; color: var(--white); white-space: nowrap;
  }

  .enroll {
    position: absolute; left: 0; top: 1040px; width: 517px; text-align: center;
    font-family: "Roboto Condensed", sans-serif; color: var(--black);
  }
  .enroll-line { font-size: 23px; line-height: 30px; }
  .enroll-line a { color: var(--link-blue); text-decoration: none; }
  .enroll-contact { font-size: 20px; line-height: 30px; color: var(--footer-blue); margin-top: 2px; }

  .testimonials-shape { position: absolute; left: 517px; top: 605px; }
  .testimonials {
    position: absolute; left: 517px; top: 634px; width: 316px;
  }
  .quote-mark {
    position: absolute; left: 12px; top: -6px;
    font-family: "Roboto", sans-serif; font-weight: 900; font-size: 120px; line-height: 1;
    color: var(--black);
  }
  .testimonials-heading {
    position: absolute; left: 108px; top: 8px; width: 205px;
    font-family: "Pacifico", cursive; font-weight: 400; font-size: 19px; line-height: 34px;
    color: var(--black); white-space: nowrap;
  }
  .quotes {
    position: absolute; left: 16px; top: 92px; width: 290px; list-style: none;
    font-family: "Roboto Condensed", sans-serif; font-size: 16.5px; line-height: 21px; color: var(--black);
  }
  .quotes li { padding-bottom: 12px; margin-bottom: 14px; border-bottom: 3px solid var(--black); }
  .quotes li:last-child { border-bottom: none; }

  .fees {
    position: absolute; left: 517px; top: 1034px; width: 365px; height: 106px;
    background: var(--black); text-align: center;
    font-family: "Roboto Condensed", sans-serif; font-size: 20px; line-height: 30px;
    color: var(--footer-cyan); padding-top: 8px;
  }
</style>
</head>
<body>
<main class="flyer">
  <section class="hero">
    <div class="hero-art" role="img" aria-label="Photo of a thoughtful young professional in a suit with arms crossed, framed by two hand-drawn robotic wrench arms"></div>
    <div class="title-band"></div>
    <div class="title-design">DESIGN</div>
    <div class="title-thinking">THINKING</div>
    <div class="title-course">COURSE</div>
    <p class="tagline tagline-one">DESIGNING YOUR WAY</p>
    <p class="tagline tagline-two">TO BETTER <strong>SOLUTIONS.</strong></p>
  </section>

  <h1 class="hosts">Maple Ridge Public Schools and Summit Valley BOCES</h1>
  <p class="intro">invite you todiscover the power of Design Thinking.&nbsp; During our three sessioncourse, you will learn and practice mindsets and tools that help you continuously and creatively improve the experiences of the people you serve by:</p>
  <ul class="benefits">
    <li>Understanding what your teachers, students and community truly need in their learning and work experiences</li>
    <li>Designing solutions that better meet their needs</li>
    <li>Seeking authentic feedback and reactions to these solutions prior to their implementation.</li>
  </ul>

  <section class="schedule">
    <h2 class="schedule-heading">We are offering this three-session course<br>at four different times in winter 2017.</h2>
    <ul class="sessions">
      <li><span class="day">Mondays</span><span class="start">- 8:30 a.m.</span>to 12:00 p.m.</li>
      <li><span class="day">Tuesdays</span><span class="start">- 12:30 p.m.</span>to 4:00 p.m.</li>
      <li><span class="day">Wednesdays</span><span class="start">- 12:30 p.m.</span>to 4:00 p.m.</li>
      <li><span class="day">Wednesdays</span><span class="start">- 4:00 p.m.</span>to 7:30 p.m.</li>
    </ul>
    <p class="schedule-note">This course is held in Maple Ridge Public Schools. No fee for MRPS leaders,</p>
  </section>

  <section class="enroll">
    <p class="enroll-line">Who can enroll Go to <a href="#">www.svboces.org</a> to learn more.</p>
    <p class="enroll-contact">Would have Questions?&nbsp; info@svboces.org</p>
  </section>

  <svg class="testimonials-shape" width="316" height="429" viewBox="0 0 316 429" aria-hidden="true">
    <polygon points="0,29 316,0 316,429 0,429" fill="var(--lime)"/>
  </svg>
  <section class="testimonials">
    <div class="quote-mark" aria-hidden="true">&ldquo;</div>
    <h2 class="testimonials-heading">What our<br>participants say…</h2>
    <ul class="quotes">
      <li>“This has been an empowering experience that allowed me to try out dramatic changes in my practice that I wouldn’t have imagined before.”</li>
      <li>“I never realized how often I’ve guessed and assumed what our teachers and students need – now I have a way to stop guessing!”</li>
      <li>“I finally have tools to generate truly creative ideas that people actually embrace… because they meet their needs”</li>
    </ul>
  </section>

  <section class="fees">
    <p>$150 fee for leaders outside of MRPS,</p>
    <p>https://forms.svboces.org</p>
  </section>
</main>
</body>
</html>
```